Email signature design - law firm

We are a small boutique law firm which is located near the beach in Manly, Australia.

We have just recently developed a new logo and are looking to redesign our letterhead, business cards and email signatures.

This brief is for our email signatures. This is an email signature to appear at the bottom of our Outlook emails so we would like it to be text that we are able to edit as the wording in our email signature often required amendments.

I have attached a word document which had our new logo, and our previous email signature which all the information/wording that needs to be included.

We would like multiple designs with a modern, simplistic yet striking look.

Thanks.

font - raleway or montserrat

Need extra days to review

• Must have the exact wording which appears in the email signature in the word document attached to brief.
• Must be able to edit the text as it is for an Outlook email signature which wording will change from time to time.

```html
<!DOCTYPE html>
<html lang="en">
<head>
<meta charset="utf-8">
<title>Harbourne &amp; Partners – Signature and Letterhead</title>
<link href="https://fonts.googleapis.com/css2?family=Raleway:wght@700;800&family=Open+Sans:wght@400;600&display=swap" rel="stylesheet">
<style>
  :root {
    --backdrop: #9e9e9e;
    --paper: #fafafa;
    --ink: #222222;
    --ink-soft: #555555;
    --navy: #1f3370;
    --blue-light: #5b7bbd;
    --brand-blue: #3b4f9a;
    --gold: #b7a477;
    --gold-grey: #8a8268;
    --white: #ffffff;
  }
  html, body {
    margin: 0;
    padding: 0;
    width: 939px;
    height: 1200px;
    overflow: hidden;
    background: var(--backdrop);
  }
  .stage {
    position: relative;
    width: 1139px;
    height: 1455px;
    transform: scale(0.8244);
    transform-origin: 0 0;
    font-family: "Open Sans", Arial, sans-serif;
  }
  .sheet {
    position: absolute;
    left: 207px;
    width: 725px;
    background: var(--paper);
    overflow: hidden;
    box-shadow: 0 0 0 1px #d6d6d6;
  }
  .signature { top: 93px; height: 189px; }
  .letterhead { top: 321px; height: 1026px; }

  .contact-panel {
    position: absolute;
    right: 0;
    bottom: 0;
    background: linear-gradient(90deg, var(--blue-light) 0%, #344c8e 45%, var(--navy) 100%);
  }
  .gold-strip {
    position: absolute;
    left: 0;
    bottom: 0;
    background: linear-gradient(90deg, var(--gold), var(--gold-grey));
  }
  .signature .contact-panel { left: 330px; height: 92px; }
  .signature .gold-strip { right: 395px; height: 12px; }
  .letterhead .contact-panel { left: 380px; height: 118px; }
  .letterhead .gold-strip { right: 345px; height: 16px; }

  .firm {
    position: absolute;
    display: flex;
    align-items: center;
    gap: 12px;
    font-family: "Raleway", Arial, sans-serif;
    font-weight: 800;
    color: var(--ink);
    letter-spacing: 1.6px;
    white-space: nowrap;
  }
  .firm-dot {
    border-radius: 50%;
    background: var(--brand-blue);
    flex: none;
  }
  .signature .firm { left: 110px; top: 22px; font-size: 20px; }
  .signature .firm-dot { width: 36px; height: 36px; }
  .letterhead .firm {
    left: 58px; top: 70px;
    flex-direction: column;
    align-items: flex-start;
    gap: 40px;
    font-size: 14.5px;
    letter-spacing: 1.2px;
  }
  .letterhead .firm-dot { width: 56px; height: 56px; margin-left: 6px; }
  .person {
    position: absolute;
    left: 76px; top: 90px;
    width: 220px;
    text-align: center;
  }
  .person-name {
    font-family: "Raleway", Arial, sans-serif;
    font-weight: 700;
    font-size: 20px;
    color: var(--brand-blue);
    line-height: 1.2;
  }
  .person-role {
    font-size: 11px;
    color: var(--ink);
    margin-top: 3px;
  }
  .address {
    position: absolute;
    color: var(--ink-soft);
    line-height: 1.3;
  }
  .signature .address { right: 35px; top: 18px; font-size: 13.5px; text-align: right; }
  .letterhead .address { left: 70px; top: 899px; font-size: 14px; }
  .contacts {
    position: absolute;
    margin: 0; padding: 0;
    list-style: none;
    color: var(--white);
    text-align: right;
  }
  .contacts li {
    display: flex;
    justify-content: flex-end;
    align-items: center;
    gap: 7px;
  }
  .contacts svg { width: 11px; height: 11px; fill: var(--white); flex: none; }
  .signature .contacts { right: 36px; top: 107px; font-size: 12.5px; line-height: 17px; }
  .letterhead .contacts { right: 59px; top: 924px; font-size: 14px; line-height: 19.5px; }
  .letterhead .contacts svg { width: 12px; height: 12px; }
</style>
</head>
<body>
<div class="stage">

  <svg width="0" height="0" style="position:absolute" aria-hidden="true">
    <defs>
      <symbol id="icon-phone" viewBox="0 0 12 12">
        <path d="M1 4c0-2 2-3 5-3s5 1 5 3l-2.5.6L8 3.4H4L3.5 4.6ZM3 5h6l2 5H1Z"/>
      </symbol>
      <symbol id="icon-mail" viewBox="0 0 12 12">
        <path d="M0 2.5h12v7H0Zm1 1v.3l5 3.2 5-3.2v-.3Z"/>
      </symbol>
      <symbol id="icon-globe" viewBox="0 0 12 12">
        <path d="M6 .5a5.5 5.5 0 1 0 0 11 5.5 5.5 0 0 0 0-11Zm0 1c.8.8 1.3 2.2 1.4 3.8H4.6C4.7 3.7 5.2 2.3 6 1.5Zm-3.4 3.8H1.6a4.5 4.5 0 0 1 2.6-3.5c-.6 1-1 2.2-1.1 3.5Zm0 1.4c.1 1.3.5 2.5 1.1 3.5a4.5 4.5 0 0 1-2.6-3.5Zm2 0h2.8C7.3 8.3 6.8 9.7 6 10.5c-.8-.8-1.3-2.2-1.4-3.8Zm4.8 0h1a4.5 4.5 0 0 1-2.6 3.5c.6-1 1-2.2 1.1-3.5Zm0-1.4c-.1-1.3-.5-2.5-1.1-3.5a4.5 4.5 0 0 1 2.6 3.5Z"/>
      </symbol>
    </defs>
  </svg>

  <section class="sheet signature" aria-label="Email signature">
    <div class="gold-strip" role="img" aria-label="Decorative gold band"></div>
    <div class="contact-panel" role="img" aria-label="Decorative navy band behind contact details"></div>
    <div class="firm"><span class="firm-dot"></span>Harbourne &amp; Partners</div>
    <div class="person">
      <div class="person-name">Maya Ellison</div>
      <div class="person-role">Managing Director</div>
    </div>
    <div class="address">Suite 4, 12 Tidewater Lane<br>Seacliff NSW 2099</div>
    <ul class="contacts">
      <li>(02) 5550 1240 <svg><use href="#icon-phone"/></svg></li>
      <li>(02) 5550 1241 <svg><use href="#icon-phone"/></svg></li>
      <li>maya.ellison@coastlaw.com.au <svg><use href="#icon-mail"/></svg></li>
      <li>www.harbournepartners.com.au <svg><use href="#icon-globe"/></svg></li>
    </ul>
  </section>

  <section class="sheet letterhead" aria-label="Letterhead">
    <div class="gold-strip" role="img" aria-label="Decorative gold band"></div>
    <div class="contact-panel" role="img" aria-label="Decorative navy band behind contact details"></div>
    <div class="firm"><span class="firm-dot"></span>Harbourne &amp; Partners</div>
    <div class="address">Suite 4, 12 Tidewater Lane<br>Seacliff NSW 2099</div>
    <ul class="contacts">
      <li>(02) 5550 1240 <svg><use href="#icon-phone"/></svg></li>
      <li>(02) 5550 1241 <svg><use href="#icon-phone"/></svg></li>
      <li>maya.ellison@coastlaw.com.au <svg><use href="#icon-mail"/></svg></li>
      <li>www.harbournepartners.com.au <svg><use href="#icon-globe"/></svg></li>
    </ul>
  </section>

</div>
</body>
</html>
```